DL, Tri Fold Flyer - Curious Kettle Lab

We need DL Tri Fold Brochure designed to print and distribute to primary schools in Australia advertising our exciting and educational science workshops.

Fun, exciting yet with a professional/educational edge. Similar to the feel of our website science shop www.curiouskettlelab.com.au and/or incursion page curiouskettlelabvisits.com.au

Design should be fresh, clean and simple, eye-catching with a sense of quality.

There needs to be visual interest with graphic elements and pictures to break up the text. To be print ready with bleed and cut lines indicated for printer. Roll fold, 2 -sided, and full colour.

The font cover image spills on to the back cover and needs to relate to the Boffin Days theme for 2020: Innovations for the future of our oceans. Perhaps eye-catching offshore ocean turbines (with or without ocean life underneath)? Example images attached, can use an image from Pixelbarn library.

This is a link to brochures printed in the past to give you an idea of design and layout.

Can use images of our presenters/kids on friendloop page to break up text - www.friendloop.com/curiouskettlelab

Please see the attached file CuriousKettleLabBrochureDesignBrief2020 for complete text and layout requirements - this file is coming soon.

Target Market(s)

Primary School Teachers

Colors

Designer to choose colors to be used in the design.

Requirements
Must have
• 1. Eye-catching front image picture, spilling on to back cover
• 2. Quality feel
• 3. Images to break up text

```html
<!DOCTYPE html>
<html lang="en">
<head>
<meta charset="utf-8">
<title>Curious Kettle Lab – 2020 DL Tri-Fold Brochure</title>
<link href="https://fonts.googleapis.com/css2?family=Montserrat:wght@700;800&family=Open+Sans:wght@400;600;700&display=swap" rel="stylesheet">
<style>
:root{
  --navy:#1f2f6b;
  --red:#d31f2f;
  --sky:#2e9ad6;
  --sky-light:#7ec8f0;
  --ink:#2b2b35;
  --muted:#555a66;
  --on-navy:#e4e8f5;
  --paper:#ffffff;
  --paper-grey:#f0f0f2;
  --stage:#e4e2de;
}
*{box-sizing:border-box;margin:0;padding:0}
html,body{width:1200px;height:1200px;overflow:hidden}
body{background:var(--stage);font-family:"Open Sans",Arial,sans-serif;color:var(--ink);position:relative}
.spread{position:absolute;left:195px;width:810px;height:573px;display:flex;box-shadow:0 2px 8px rgba(0,0,0,.18)}
.spread--outside{top:18px}
.spread--inside{top:609px}
.panel{position:relative;width:270px;height:573px;overflow:hidden;background:var(--paper)}
.panel--grey{background:var(--paper-grey)}
.panel__bg{position:absolute;inset:0;width:270px;height:573px}
.panel__content{position:relative;padding:18px 16px 0}
.section-title{font-family:"Montserrat",Arial,sans-serif;font-weight:800;font-size:8.5px;letter-spacing:.6px;text-transform:uppercase;color:var(--sky);margin-bottom:8px}
.section-title--light{color:var(--sky-light)}
.entry{margin-bottom:7px}
.entry__head{font-size:5.8px;font-weight:700;color:var(--red)}
.entry__head span{color:var(--navy)}
.entry__text{font-size:5.2px;line-height:1.38;color:var(--muted);text-align:justify}
.body{font-size:5.4px;line-height:1.4;text-align:justify;margin-bottom:6px;color:var(--muted)}
.on-navy .entry__text,.on-navy .body{color:var(--on-navy)}
.on-navy .entry__head span{color:#fff}
.on-navy .entry__head{color:#ff6b73}
.on-navy .body--strong{color:#fff;font-weight:700}
.subhead{font-size:6px;font-weight:700;text-transform:uppercase;margin:8px 0 4px;color:#fff}
.price-row{display:flex;gap:8px;margin:6px 0}
.price-box{border:1px solid #fff;padding:3px 5px;font-size:5px;color:#fff;width:80px;line-height:1.3}
.brand{display:flex;align-items:center;gap:4px;font-family:"Montserrat",sans-serif;font-weight:800;color:var(--navy)}
.brand__dot{width:10px;height:10px;border-radius:50%;background:var(--sky);flex:none}
/* cover */
.cover-year{position:absolute;top:20px;left:0;width:270px;text-align:center;font-family:"Montserrat",sans-serif;font-weight:800;font-size:22px;color:var(--red)}
.cover-kicker{position:absolute;top:50px;left:0;width:270px;text-align:center;font-family:"Montserrat",sans-serif;font-weight:800;font-size:9px;line-height:1.35;color:#fff;letter-spacing:.3px}
.cover-title{position:absolute;top:80px;left:0;width:270px;text-align:center;font-family:"Montserrat",sans-serif;font-weight:800;font-size:15px;line-height:1.05;color:#fff;letter-spacing:.6px}
.cover-brand{position:absolute;top:372px;left:0;width:270px;justify-content:center;font-size:12px}
.cover-pill{position:absolute;top:400px;left:42px;width:186px;height:18px;background:var(--sky);color:#fff;text-align:center;font-family:"Montserrat",sans-serif;font-weight:800;font-size:9.5px;line-height:18px;border-radius:2px}
.cover-call{position:absolute;top:424px;left:0;width:270px;text-align:center;font-family:"Montserrat",sans-serif;font-weight:700;font-size:9px;color:var(--ink)}
.cover-hours{position:absolute;top:440px;left:0;width:270px;text-align:center;font-size:6px;line-height:1.4;color:var(--ink)}
.cover-url{position:absolute;top:466px;left:14px;width:242px;height:22px;background:var(--red);border-radius:3px;color:#fff;text-align:center;font-weight:700;font-size:7px;line-height:22px}
/* booking */
.booking{position:absolute;top:352px;left:14px;width:122px}
.booking .brand{font-size:6.5px;margin-bottom:12px}
.booking h4{font-family:"Montserrat",sans-serif;font-size:6px;color:var(--red);text-transform:uppercase;margin-bottom:5px}
.booking p{font-size:5.4px;line-height:1.45;margin-bottom:6px;color:var(--ink)}
.why-box{position:absolute;top:325px;left:142px;width:116px;height:226px;background:var(--red);border-radius:6px;padding:9px;color:#fff}
.why-box h5{font-size:6px;font-weight:700;margin-bottom:5px;color:#ffe0e2}
.why-box .price-box{border-color:#ffb3b8;width:auto;margin-bottom:4px}
.why-box ul{list-style:none;font-size:5.4px;line-height:1.35}
.why-box li{display:flex;gap:3px;margin-bottom:3px}
.why-box li::before{content:"✓";font-weight:700}
.url-foot{position:absolute;bottom:12px;left:12px;width:246px;height:16px;background:var(--navy);border-radius:8px;color:#fff;font-size:5.6px;font-weight:600;line-height:16px;padding-left:10px}
.about-head{display:flex;align-items:center;gap:6px;margin-bottom:8px}
.about-head .brand{font-size:6px}
.about-head .section-title{margin:0}
</style>
</head>
<body>

<section class="spread spread--outside" aria-label="Brochure outside">

  <article class="panel panel--grey">
    <div class="panel__content">
      <h2 class="section-title">Physical Sciences</h2>
      <div class="entry"><div class="entry__head">Forces in Action <span>– Foundation to 6</span></div><p class="entry__text">From a falling apple to a rolling car, forces are at work everywhere. Explore spinning tops, flying toys, friction and inertia in this hands-on look at how things move, and why. Junior or senior format. VIC, NSW, QLD</p></div>
      <div class="entry"><div class="entry__head">Rocket Science <span>– Level 3 to 6</span></div><p class="entry__text">Brace yourself for lift off! Students explore the principles of rocket propulsion and the forces at play, then build a rocket ready for a grand launch of up to 30 metres. 90 minute format only. VIC, NSW, QLD</p></div>
      <div class="entry"><div class="entry__head">Light and Sound <span>– Foundation to Level 2</span></div><p class="entry__text">Make some waves and colour your classroom with rainbows. Using sensory activities learners explore the properties and travel of light and sound energy. VIC, NSW, QLD</p></div>
      <div class="entry"><div class="entry__head">Electrical Buzz <span>– Foundation to Level 6</span></div><p class="entry__text">Lights, noise and spinning propellers. Use snap circuit kits to build working circuits with switches, LEDs, resistors and integrated sound chips. Explore circuits, magnets, dynamos and energy changes, with a look at how power is made from sun light. VIC, NSW, QLD</p></div>
      <div class="entry"><div class="entry__head">Simple Machines <span>– Level 3 to 6</span></div><p class="entry__text">Launch projectiles with DIY catapults, watch motorised gears turn to speed things up and lift friends off the ground with a super sized lever. An engaging look at how simple machines make our life easier, now and in the past. 90 minute format only. VIC</p></div>
      <div class="entry"><div class="entry__head">Simple Machines <span>– Level 3 to 6</span></div><p class="entry__text">Launch projectiles with DIY catapults, watch motorised gears turn to speed things up and lift friends off the ground with a super sized lever. An engaging look at how simple machines make our life easier, now and in the past. 90 minute format only. VIC</p></div>
      <div class="entry"><div class="entry__head">Light &amp; Colour <span>– Foundation to Level 2</span></div><p class="entry__text">An engaging investigation into the colourful properties of light. Create rainbows, use chromatography to separate colour in ink, mix colour with light filters and test a whole host of optical instruments. VIC, NSW, QLD</p></div>
      <div class="entry"><div class="entry__head">Toy Technology <span>– Foundation to Level 2</span></div><p class="entry__text">Be immersed in the wonderful science of toys. Explore energies, materials, movement and sound. Spin some colour, use magnets to draw, and even make your very own balancing toy to take home. Play has never been so educational! VIC, NSW, QLD</p></div>
      <div class="entry"><div class="entry__head">Light Reflections <span>– Level 3 to 6</span></div><p class="entry__text">This senior primary workshop takes an in-depth look at the properties of light, within and outside the visible spectrum. Get hands-on with a variety of optical instruments, explore UV light and make a UV detection key chain to keep, watch light energy transform, and much more. VIC, NSW, QLD</p></div>
      <div class="entry"><div class="entry__head">Heat &amp; Energy <span>– Level 3 to 6</span></div><p class="entry__text">Explore the properties of heat and other energies in a fun way. Produce useful heat energy in a multitude of ways, including through friction, motion, electricity and chemicals. Transfer heat through conduction, measure it and explore the amazing ways in which heat can generate change. VIC, NSW, QLD</p></div>
    </div>
  </article>

  <article class="panel">
    <svg class="panel__bg" viewBox="0 0 270 573" aria-hidden="true">
      <path d="M0 0H270V285Q200 262 130 300Q60 340 0 318Z" fill="var(--navy)"/>
      <path d="M0 318Q60 340 130 300Q200 262 270 285V300Q200 278 132 314Q62 352 0 334Z" fill="var(--red)"/>
    </svg>
    <div class="panel__content on-navy">
      <h2 class="section-title section-title--light">Duration and Cost</h2>
      <p class="body">Our memorable science sessions come to you. No bus hire, and no other costs tied to excursions. Most of our session topics are available in either a 60 or 90 minute format to fit easily around your school timetable.</p>
      <p class="body body--strong">Costs are calculated per session for a class of up to 30 students.</p>
      <p class="body">Unless otherwise stated, the workshop prices are as follows:</p>
      <div class="price-row">
        <div class="price-box">$235 for a<br>60 minute workshop<br>plus GST</div>
        <div class="price-box">$290 for a<br>90 minute workshop<br>plus GST</div>
      </div>
      <p class="body">There is a minimum booking of 3 x 60 minute workshops or 2 x 90 minute workshops, or their cost equivalent. Cost-saving options are available, like splitting 4 sessions between 3 groups. Contact our office for full details on costs, availability and session topics.</p>
      <p class="body">Workshops delivered to schools in outer regions incur travel costs. Multiple topics in one day incur a surcharge. We ask that teachers help with supervising sessions; you might be surprised with what you learn too. A perfect professional development opportunity!</p>
      <h3 class="subhead">Kindergarten Sessions</h3>
      <p class="body">Based on a play-based approach suited to pre-school children, six workstations are set up to engage children in a variety of open-ended science activities. Themes such as magnetism, electricity, chemistry, forces, light &amp; colour and mini beasts are included. Children use the materials at their own pace, supported by the presenter and kindergarten staff. Parent helpers are welcome, ideally one adult per workstation.</p>
    </div>
    <div class="booking">
      <div class="brand"><span class="brand__dot"></span>Curious Kettle Lab</div>
      <h4>Book a workshop<br>&amp; more info</h4>
      <p><b>Call Us 1300 555 019<br>Mon to Fri 9:30 till 3pm</b></p>
      <p>info@curiouskettlelab.com.au<br>curiouskettlelabvisits.com.au</p>
      <p>Postal Address:<br>PO Box 118, Larkfield, VIC, 3188<br>Physical Address:<br>4/27 Wattle Ridge Rd, Larkfield,<br>VIC, 3188</p>
    </div>
    <div class="why-box">
      <h5>The cost for a group of up to 30 students is:</h5>
      <div class="price-box">$160 for a single 60 or 90 minute kindergarten workshop plus GST</div>
      <div class="price-box">$290 for two or more consecutive 60 or 90 minute kindergarten workshops plus GST</div>
      <h5 style="margin-top:6px">Why Choose Us?</h5>
      <ul>
        <li>Seriously fun, and engaging</li>
        <li>Lead by science teaching specialists</li>
        <li>Packed full of hands-on experimenting</li>
        <li>Aligned with curriculum outcomes</li>
      </ul>
    </div>
  </article>

  <article class="panel">
    <svg class="panel__bg" viewBox="0 0 270 573" aria-hidden="true">
      <defs>
        <linearGradient id="sunsetCover" x1="0" y1="0" x2="0" y2="1">
          <stop offset="0" stop-color="#3b2a22"/>
          <stop offset=".45" stop-color="#e79a3a"/>
          <stop offset=".6" stop-color="#f6c35c"/>
          <stop offset=".75" stop-color="#b55a1c"/>
          <stop offset="1" stop-color="#2a1a12"/>
        </linearGradient>
      </defs>
      <path d="M0 0H270V290Q160 300 90 330Q40 350 0 340Z" fill="var(--navy)"/>
      <path d="M0 340Q40 350 90 330Q160 300 270 290V312Q170 318 100 348Q45 372 0 362Z" fill="var(--red)"/>
      <circle cx="135" cy="225" r="108" fill="var(--red)"/>
      <circle cx="135" cy="225" r="100" fill="url(#sunsetCover)" role="img" aria-label="Photo: offshore wind turbines silhouetted against a golden sunset over the ocean"/>
    </svg>
    <div class="cover-year">2020</div>
    <div class="cover-kicker">PRIMARY SCHOOL SCIENCE<br>WORKSHOPS &amp; INCURSIONS</div>
    <div class="cover-title">THE POWER<br>OF THE DEEP BLUE</div>
    <div class="brand cover-brand"><span class="brand__dot"></span>Curious Kettle Lab</div>
    <div class="cover-pill">NOW IN QLD AND NSW!</div>
    <div class="cover-call">CALL US 1300 555 019</div>
    <div class="cover-hours">Mon to Fri 9:30 till 3pm<br>Inquire by email info@curiouskettlelab.com.au</div>
    <div class="cover-url">www.curiouskettlelabvisits.com.au</div>
  </article>
</section>

<section class="spread spread--inside" aria-label="Brochure inside">

  <article class="panel panel--grey">
    <div class="panel__content">
      <h2 class="section-title">Biological Sciences</h2>
      <div class="entry"><div class="entry__head">Living Things <span>– Foundation to Level 6</span></div><p class="entry__text">This workshop is full of life. Explore objects that have self-sustaining processes like plants, animals and micro-organisms. Through engaging hands-on activities learn about the difference between living and non-living things, simple life cycles and the bigger picture. Junior or senior format. VIC, NSW, QLD</p></div>
      <div class="entry"><div class="entry__head">Senses <span>– Foundation to Level 2</span></div><p class="entry__text">The five senses are given a workout in this engaging session. They are tested, tricked and more. VIC, NSW, QLD</p></div>
      <div class="entry"><div class="entry__head">The Human Body <span>– Level 3 to 6</span></div><p class="entry__text">Take a journey through the human body and explore its parts and systems. Perform chemical experiments to understand digestion, think quick and test reaction speeds, use stethoscopes to listen to the rhythmic beat of your heart. Learn how we are all connected and made of the stuff of stars! VIC, NSW, QLD</p></div>
      <h2 class="section-title" style="margin-top:12px">Earth and Space Sciences</h2>
      <div class="entry"><div class="entry__head">Wicked Weather <span>– Foundation to Level 2</span></div><p class="entry__text">Air in the atmosphere is always on the move, carrying clouds, rain and snow around the globe. Model and experiment with the air and water movements and even make your own flurry of snow. VIC, NSW, QLD</p></div>
      <div class="entry"><div class="entry__head">Natural Disasters <span>– Level 3 to 6</span></div><p class="entry__text">Explore the scientific processes behind the explosive energy of nature's fury. VIC, NSW, QLD</p></div>
      <div class="entry"><div class="entry__head">Global Sustainability <span>– Level 1 to 6</span></div><p class="entry__text">The global population boom in recent times has put the Earth's resources under great strain. Learn how we can better manage waste and the Earth's life sustaining resources to build a better future for all. VIC, NSW, QLD</p></div>
      <div class="entry"><div class="entry__head">Earth &amp; The Milky Way <span>– Level 3 to 6</span></div><p class="entry__text">Space is a vacuum but it is far from empty. During this fascinating workshop you'll launch into space and explore planets, moons, stars and galaxies. Follow in the footsteps of the great astronomers as you explore the mystery, scale and Earth's place in the universe. VIC, NSW, QLD</p></div>
      <div class="entry"><div class="entry__head">Rocks &amp; Geology <span>– Level 3 to 6</span></div><p class="entry__text">History is written in the rocks. Read the changing story of Earth and the impact of humans through the pages of rocks. Get your own fossil, explore and classify rocks and minerals, investigate the characteristics of soil, model the layers of earth, create some explosive lava. Everything to enthuse young geologists. VIC</p></div>
      <div class="entry"><div class="entry__head">Water &amp; The Environment <span>– Foundation to Level 4</span></div><p class="entry__text">Water is essential to life, and is our most precious resource. We use it to drink, for cooking, washing and hygiene, recreation, industry and agriculture. During this workshop students develop an understanding and appreciation of the importance and special properties of water. VIC, NSW, QLD</p></div>
    </div>
    <div class="url-foot">www.curiouskettlelabvisits.com.au</div>
  </article>

  <article class="panel">
    <svg class="panel__bg" viewBox="0 0 270 573" aria-hidden="true">
      <defs>
        <linearGradient id="skyInside" x1="0" y1="0" x2="0" y2="1">
          <stop offset="0" stop-color="#2f7fc4"/>
          <stop offset=".55" stop-color="#b9dcf2"/>
          <stop offset=".7" stop-color="#5a8fb8"/>
          <stop offset="1" stop-color="#1d4f7d"/>
        </linearGradient>
      </defs>
      <rect width="270" height="573" fill="var(--navy)"/>
      <path d="M0 470Q120 380 270 395V573H0Z" fill="var(--red)"/>
      <path d="M0 482Q120 392 270 408V573H0Z" fill="url(#skyInside)" role="img" aria-label="Photo: white offshore wind turbines standing in a blue sea under a clear sky"/>
    </svg>
    <div class="panel__content on-navy">
      <h2 class="section-title section-title--light">STEM – Science, Technology,<br>Engineering &amp; Mathematics</h2>
      <div class="entry"><div class="entry__head">The Power of the Deep Blue <span>– Foundation to Level 6 NEW!</span></div><p class="entry__text">Our oceans are teeming with life in various marine environments. They are the heritage, heart and economic future of our country. This workshop takes a deep dive into sustainable seafood and renewable energy production for a marine nation. Available in a junior or senior format. VIC, NSW, QLD</p></div>
      <div class="entry"><div class="entry__head">Buzzbot Robotics <span>– Foundation to Level 2</span></div><p class="entry__text">An introduction to robots and programming for younger students. With an intuitive interface, colourful buzzbot will have learners excited about simple sequencing and directional language. VIC</p></div>
      <div class="entry"><div class="entry__head">Buzzbot Robotics Programming <span>– Level 3 to 6</span></div><p class="entry__text">Meet friendly Buzzbot, a STEM educational robot to learn coding and robotics. Drag-and-drop graphical programming makes learning Pinboard easy and crazy fun! Available in a 90 minute format only at $380 plus GST per session. VIC</p></div>
      <div class="entry"><div class="entry__head">Circuit Board Electronics <span>– Level 5 &amp; 6</span></div><p class="entry__text">Solder electronic components onto specially designed circuit boards. Take home your own working electronic device like an alarm, lie detector or game. Maximum 20 students. Available in a 90 minute format only at $490 plus GST per session. VIC</p></div>
      <div class="entry"><div class="entry__head">3D Drawing <span>– Level 1 to 6</span></div><p class="entry__text">This STEM workshop has you inventing and creating in 3D. Using 3D pen technology, design your own plastic model to take home. VIC</p></div>
      <div class="entry"><div class="entry__head">Lab Science Show <span>– Foundation to Level 6</span></div><p class="entry__text">A jam-packed 60 min show of BIG WOW science madness! There's giant smoke vortices, levitating beach balls, flying toilet paper, flour fire-balls, hair-raising electricity, and lots of wonder! Suitable for up to 180 students. Price $650 plus GST. VIC, NSW, QLD</p></div>
      <div class="entry"><div class="entry__head">Reactive Chemistry Show <span>– Foundation to Level 6 NEW!</span></div><p class="entry__text">Watch chemicals react in a big way! See impressive colour changes, smelly invisible gases and hear some oh-mighty noises. Learn about the conversion of reactant molecules to products and the energy changes involved, all while safely shooting foam and fire. Reactive chemistry at its exciting best! Price $710 plus GST. VIC</p></div>
    </div>
  </article>

  <article class="panel">
    <div class="panel__content">
      <div class="about-head"><div class="brand"><span class="brand__dot"></span>Curious Kettle Lab</div><h2 class="section-title">About us</h2></div>
      <p class="body">In 2020, our seriously FUN workshops will be available in VIC, QLD and NSW! Our quality science incursions are aligned with the curriculum, and blend amazing class demonstrations with hands-on experiments to facilitate genuine learning.</p>
      <p class="body">Our expert workshop facilitators present a range of incursion topics encompassing biological, chemical, earth &amp; space, and physical sciences as well as STEM workshops, from foundation to level 6. During our sessions students develop critical and creative thinking skills, they will ask questions, make predictions and draw conclusions using scientific methods.</p>
      <p class="body">The 2020 Boffin Days theme is Deep Blue: Innovations for the future of our oceans. Our new workshop The Power of the Deep Blue has been developed around this theme.</p>
      <h2 class="section-title" style="margin-top:12px">Chemical Sciences</h2>
      <div class="entry"><div class="entry__head">Chemistry Chaos <span>– Foundation to Level 6</span></div><p class="entry__text">Colour changes, smoke, fizz and foam! Everything in our world is made up of chemicals; explore fascinating polymer chemicals, chemical reactions, reversible physical changes and more. Available in a junior or senior format. VIC, NSW, QLD</p></div>
      <div class="entry"><div class="entry__head">The Matter Of Matter <span>– Level 3 to 6</span></div><p class="entry__text">Use the magic of dry ice to explore the three common states of matter: solids, liquids and gases. From everlasting bubbling fountains to cool chemical fire extinguishers. This session makes a fantastic introduction. Format only, incurs a $45 per day dry ice surcharge. VIC, NSW, QLD</p></div>
      <div class="entry"><div class="entry__head">Forensic Detective <span>– Level 3 to 6</span></div><p class="entry__text">Can you crack the case and catch the thief? Use real forensic science techniques, like PH tests, ink chromatography, glow chemicals and fingerprint dusting to pinpoint the culprit. Available in a 90 minute format only. VIC, NSW, QLD</p></div>
      <div class="entry"><div class="entry__head">Super Bubble Science <span>– Foundation to Level 2</span></div><p class="entry__text">Bubbles are more than trapped air in a film of soapy water. Their exact spherical shape and swirling rainbow colours make them a wonder of science. By this session end, you'll be a true bubbleologist. VIC, NSW, QLD</p></div>
      <div class="entry"><div class="entry__head">Kitchen Chemistry <span>– Foundation to Level 2</span></div><p class="entry__text">A fun food workshop challenging you to think about everyday food in a whole new way. Experiment with a variety of food related chemicals and you even get to take home a bag of sweet, tongue tingling sherbet! VIC, NSW, QLD</p></div>
      <div class="entry"><div class="entry__head">Material Science <span>– Foundation to Level 6</span></div><p class="entry__text">Explore the world around you: sort, classify and test the physical properties of natural and processed materials. Discover how materials can change physically as well as chemically. Use a material for a purpose, explore the effect of heat on materials, minimal waste and remake a material into a new product. VIC, NSW, QLD</p></div>
    </div>
  </article>
</section>

</body>
</html>
```